Thornbury Cleaning – Website Redesign (Clean, Modern, Trust-Focused)

Thornbury Cleaning — Homepage Redesign Brief

Project Goal

We need a complete redesign of the homepage for our cleaning business, Thornbury Cleaning.
The goal is a clean, modern, trust-building homepage that works equally well for:
• Residential clients
• Commercial clients

The page should feel polished, reliable, easy to navigate, and completely free from clutter, gimmicks, or corporate-sounding fluff.

About Us (Context)

Thornbury Cleaning has operated in Sale, Victoria for over 30 years.
Our brand is built on:
• Reliability
• Convenience
• Long-term trust
• Straightforward, no-nonsense communication

We do not want to look like a large franchise, and we do not want to look cute or playful.
The design must feel modern, practical, confident, and professional.

What We Need Designed — Homepage Only

1. Hero Section

A clean, modern hero area with:
• A simple image or clean background (no clutter, no heavy overlays).
Images from our current site may be helpful, or you may source alternatives.
• Headline suggestion (designer may refine):
“30+ Years of Commercial and Residential Cleaning in Sale”
• Sub-headline suggestion:
“Trusted by locals for three decades.”
• Primary CTA button: Get a Quote

2. Trust-Building Logos

Positioned directly beneath the hero:
• Small, neat logos of organisations we work with
(RLK, Bramwell, Eastvale Regional Care, OPM, etc.)
• A clean Starlist Reviews block (stars + review count)
• Must be compact, tidy, evenly spaced — not loud or oversized

3. Trust Block / Problem–Solution Copy

This section introduces why hiring cleaners can be stressful and why reliability matters.

Headline example:
“Call the cleaners you can count on.”

We have existing copy for this section.
Please present it in a minimal, breathable, modern layout that is easy to scan.

4. Stats / Counters Section

Three sharp, structured stat boxes:
• 92+ Recurring Clients
• 4,150+ Visits Per Year
• 265+ Pre-Sale / Exit Cleans

These should look clean and understated — not oversized or gimmicky.

5. Values Section

A short section featuring our core values:
• Be Real
• Do It Right
• Have Fun
• Make It Easy

Designer has flexibility with layout.
(Sections 5 and 6 may swap depending on what flows better.)

6. Services Preview

A simple grid or row with links to our main services:
• Commercial Cleaning
• Residential Cleaning
• Window Cleaning
• Steam Cleaning

Small icons or photos are fine — but no clip art or cartoon-style graphics.

7. Footer

A very clean, simple footer with contact details.
No clutter, no heavy visual styling.

Style Requirements

Overall Tone
• Clean
• Modern
• Minimal
• Trust-driven
• Easy to read and navigate

Do NOT use
• Clip art
• Cute or playful icons
• Flowers, sparkles, “feminine” cleaning imagery
• Heavy or overly bold corporate fonts
• Busy backgrounds
• Long paragraphs of text

Reference Material

Current Website (for copy + structure only)

https://thornburycleaning-example.com.au

Rough Canva Mock-Up (layout inspiration only)

(We will upload this separately. It’s not a final design — just a loose concept for spacing/flow.)

Logo

Please use the new Thornbury Cleaning logo (uploaded in files) or a placeholder if needed. Attached is a potential for a new logo or site colours not wedded to the idea though.

What the Homepage Should Communicate

Within seconds, a visitor should understand that:
• We are established
• We are local
• We are reliable
• We make cleaning easy
• Getting a quote is quick and simple

The homepage should feel effortless, trustworthy, and modern.

Deliverable

A complete homepage design layout suitable for WordPress.
Figma, Adobe XD, or a similar design tool is fine.

Target Market(s)

Residential and commercial clients in Sale, Victoria and surrounding Gippsland region. Typical clients include busy households, office managers, receptionists, medical centres, community organisations, local businesses, and real estate/property professionals. Clients value reliability, simplicity, and stress-free long-term cleaning support.

Industry/Entity Type

Cleaning services (Residential & Commercial)

Font styles to use
Sans Serif

Requirements
Must have
• • Clean, modern, minimal layout • A trust-driven design that highlights proof (logos, stats, reviews) near the top • Clear hierarchy and no clutter • A strong hero section with simple messaging and a clear CTA • Trust logos + Starlist Reviews block directly under the hero • Structured stats/counters section • Values section (Be Real, Do It Right, Have Fun, Make It Easy) • Services preview (Commercial, Residential, Window, Steam/Carpet) • Clean footer with contact details • Use our new Thornbury Cleaning logo (or placeholder if needed) • Easy-to-read typography and spacing • Must feel like a local, real cleaning business — not a franchise
Nice to have
• • An option with centred hero text and an option with left-aligned text • Option to preview hero section with or without a quote form • Subtle use of the navy + gold palette (not heavy or corporate) • Soft, minimal background images (not busy city skylines) • Subtle section dividers or whitespace breaks to improve flow • Slightly rounded card corners for a friendly but still modern feel
Should not have
• • No clip-art, cartoon mops, sparkles, bubbles, or generic cleaning icons • No overly bold, blocky, or corporate fonts • No “mega-city” skylines (we are a regional/rural business) • No heavy overlays, dark gradients, or cluttered hero images • No long paragraphs or dense text blocks • No template-style designs that look generic or AI-generated • No overly feminine, overly masculine, or overly playful designs • No neon colors or high-saturation palettes

```html
<!DOCTYPE html>
<html lang="en">
<head>
<meta charset="utf-8">
<title>Thornbury Cleaning – Commercial and Residential Cleaning in Sale</title>
<link rel="stylesheet" href="https://fonts.googleapis.com/css2?family=Poppins:wght@400;500;600;700&display=swap">
<style>
:root{
  --navy:#12305a;
  --navy-dark:#0c2142;
  --navy-deep:#0a1a33;
  --gold:#b08d43;
  --gold-light:#c9a75e;
  --ink:#1d2433;
  --muted:#5d6675;
  --line:#e3e6ec;
  --pale:#eef3f9;
  --white:#ffffff;
}
*{box-sizing:border-box;margin:0;padding:0}
html,body{width:1200px;height:3712px;overflow:hidden}
body{font-family:"Poppins",Arial,sans-serif;color:var(--ink);background:var(--white)}
a{color:inherit;text-decoration:none}

/* Navigation */
.site-nav{height:48px;display:flex;align-items:center;justify-content:space-between;padding:0 120px 0 140px;background:var(--white);position:relative;z-index:3}
.brand{display:flex;flex-direction:column;line-height:1}
.brand-name{font-weight:700;font-size:17px;color:var(--navy);letter-spacing:.5px}
.brand-sub{font-size:8px;color:var(--gold);letter-spacing:3px;margin-top:2px}
.nav-links{display:flex;gap:6px;font-size:12px;font-weight:500;color:var(--ink)}
.nav-links a{padding:5px 10px;border-radius:3px}
.nav-links a.active{background:var(--gold);color:var(--white)}

/* Hero */
.hero{height:612px;position:relative;overflow:hidden}
.hero-photo{position:absolute;inset:0;background:linear-gradient(120deg,#dfe6ec 0%,#c9d4dd 45%,#aebdca 70%,#8f9fae 100%)}
.hero-stripe{position:absolute;inset:0;background:#2a5d94;clip-path:polygon(0 0,50% 0,36% 100%,0 100%)}
.hero-panel{position:absolute;inset:0;background:linear-gradient(160deg,var(--navy) 0%,var(--navy-dark) 100%);clip-path:polygon(0 0,46% 0,32% 100%,0 100%)}
.hero-copy{position:absolute;left:140px;top:72px;width:420px;color:var(--white)}
.hero-copy h1{font-size:44px;line-height:1.18;font-weight:700}
.hero-copy h1 span{color:var(--gold-light)}
.hero-copy p{font-size:17px;margin-top:18px;opacity:.95}
.btn-gold{display:inline-block;background:var(--gold);color:var(--white);font-size:14px;font-weight:600;padding:11px 22px;border-radius:4px;margin-top:28px}
.hero-dots{position:absolute;right:140px;bottom:24px;display:flex;gap:8px}
.hero-dots span{width:14px;height:14px;border-radius:50%;background:var(--white);opacity:.6}
.hero-dots span.on{opacity:1}

/* Trust */
.trust{height:420px;padding-top:72px}
.partner-row{display:flex;justify-content:space-between;align-items:center;width:1000px;margin:0 auto}
.partner{width:170px;height:72px;border:1px solid var(--line);border-radius:8px;display:flex;align-items:center;justify-content:center;gap:8px;font-weight:600;font-size:15px;color:var(--navy);text-align:center;padding:0 10px}
.partner i{width:14px;height:14px;border-radius:50%;background:var(--navy);flex:none}
.rating-block{width:170px;text-align:center}
.rating-block strong{display:block;font-size:22px;color:var(--navy);font-weight:600}
.rating-block em{font-style:normal;font-size:13px;color:var(--muted)}
.stars{color:#f3b32a;font-size:13px;letter-spacing:1px}
.review-strip{position:relative;width:1060px;margin:32px auto 0;display:flex;justify-content:center;gap:24px}
.review-card{width:300px;height:200px;background:var(--white);box-shadow:0 4px 16px rgba(12,33,66,.12);border-radius:8px;padding:20px}
.review-head{display:flex;align-items:center;gap:12px}
.avatar{width:40px;height:40px;border-radius:50%;background:var(--gold);color:var(--white);font-weight:600;display:flex;align-items:center;justify-content:center}
.review-head b{font-size:14px;font-weight:600}
.review-card p{font-size:11.5px;line-height:1.55;color:var(--muted);margin:10px 0 10px 52px}
.review-foot{display:flex;gap:10px;align-items:center;margin-left:0}
.review-foot i{width:14px;height:14px;border-radius:50%;border:2px solid var(--navy)}
.slider-arrow{position:absolute;top:84px;width:28px;height:28px;border-radius:50%;background:#e8ebf0;display:flex;align-items:center;justify-content:center}
.slider-arrow.prev{left:0}.slider-arrow.next{right:0}

/* About */
.about{height:648px;display:flex;align-items:center;padding:0 140px;gap:60px}
.about-photo{width:460px;height:480px;border-radius:240px 0 0 240px;background:linear-gradient(135deg,#dce3ea 0%,#b7c4d1 55%,#8ea0b3 100%);border:6px solid var(--navy);border-right:none;flex:none}
.about-copy h2{font-size:40px;line-height:1.15;color:var(--navy);font-weight:700}
.about-copy p{font-size:13px;line-height:1.65;color:var(--muted);margin-top:16px}
.btn-navy{display:inline-block;background:var(--navy);color:var(--white);font-size:13px;font-weight:600;padding:10px 20px;border-radius:4px;margin-top:22px}

/* Stats */
.stats{height:204px;display:flex}
.stat{flex:1;display:flex;align-items:center;justify-content:center;gap:18px;color:var(--white)}
.stat:nth-child(1){background:var(--navy-dark)}
.stat:nth-child(2){background:linear-gradient(120deg,var(--gold) 0%,#8d6f2f 100%)}
.stat:nth-child(3){background:linear-gradient(120deg,var(--navy) 0%,#1f5a8e 100%)}
.stat-icon{width:64px;height:64px;border-radius:50%;background:var(--white);display:flex;align-items:center;justify-content:center}
.stat strong{display:block;font-size:36px;font-weight:600;line-height:1.1}
.stat span{font-size:15px}

/* Services */
.services{height:980px;padding-top:110px;background:linear-gradient(#fff 70%,#f1f2f4 100%)}
.section-title{text-align:center;font-size:40px;color:var(--navy);font-weight:600}
.service-grid{width:920px;margin:36px auto 0;display:grid;grid-template-columns:1fr 1fr;gap:24px}
.service-card{height:320px;border-radius:10px;position:relative;overflow:hidden;box-shadow:0 6px 18px rgba(12,33,66,.15)}
.service-card.featured{outline:5px solid var(--gold-light)}
.service-card:nth-child(1){background:linear-gradient(135deg,#d8c7a8,#8c9fb6)}
.service-card:nth-child(2){background:linear-gradient(135deg,#c8d2dc,#7d8b99)}
.service-card:nth-child(3){background:linear-gradient(135deg,#bcd0e4,#3f6a9a)}
.service-card:nth-child(4){background:linear-gradient(135deg,#d9dfe5,#6c8b5f)}
.service-label{position:absolute;left:0;bottom:0;width:56%;height:44px;background:var(--navy);color:var(--white);border-radius:0 24px 0 0;display:flex;align-items:center;justify-content:center;font-size:14px;font-weight:600}

/* Values */
.values{height:496px;background:var(--pale);padding-top:124px}
.value-row{width:920px;margin:40px auto 0;display:flex;justify-content:space-between}
.value-card{width:212px;height:190px;background:var(--white);border-radius:6px;padding:26px 20px;text-align:center}
.value-card.featured{border:3px solid var(--gold-light);box-shadow:0 8px 22px rgba(12,33,66,.18)}
.value-card svg{display:block;margin:0 auto 12px}
.value-card h3{font-size:17px;font-weight:600;color:var(--navy)}
.value-card p{font-size:13px;color:var(--muted);margin-top:6px;line-height:1.45}

/* Footer */
.site-footer{height:304px;background:var(--navy-deep);color:var(--white);padding:72px 140px 0}
.contact-row{display:flex;justify-content:space-between}
.contact-item{display:flex;gap:14px;align-items:flex-start}
.contact-icon{width:44px;height:44px;border-radius:50%;background:var(--white);display:flex;align-items:center;justify-content:center;flex:none}
.contact-item b{display:block;font-size:14px;font-weight:600}
.contact-item span{font-size:13px;line-height:1.5;opacity:.9}
.footer-base{display:flex;justify-content:space-between;align-items:center;margin-top:64px;border-top:1px solid rgba(255,255,255,.15);padding-top:24px}
.footer-base .brand-name{color:var(--white)}
.footer-base small{font-size:13px;opacity:.9}
</style>
</head>
<body>

<header class="site-nav">
  <a class="brand" href="#"><span class="brand-name">THORNBURY CLEANING</span><span class="brand-sub">SALE · VIC</span></a>
  <nav class="nav-links">
    <a class="active" href="#">Home</a><a href="#">Commercial</a><a href="#">Residential</a><a href="#">Window Cleaning</a><a href="#">Steam Cleaning</a><a href="#">Contact</a><a href="#">Areas</a>
  </nav>
</header>

<section class="hero">
  <div class="hero-photo" role="img" aria-label="Cleaner steam cleaning carpet in a bright glass-walled office"></div>
  <div class="hero-stripe"></div>
  <div class="hero-panel"></div>
  <div class="hero-copy">
    <h1><span>30+</span> Years of Commercial and Residential Cleaning in Sale</h1>
    <p>Trusted by locals for three decades.</p>
    <a class="btn-gold" href="#">Get a Quote</a>
  </div>
  <div class="hero-dots"><span class="on"></span><span></span><span></span></div>
</section>

<section class="trust">
  <div class="partner-row">
    <div class="partner"><i></i>RLK Institute</div>
    <div class="partner">Bramwell</div>
    <div class="partner"><i></i>Eastvale Regional Care</div>
    <div class="partner">OPM</div>
    <div class="rating-block"><strong>Starlist</strong><em>Reviews</em><div class="stars">★★★★★</div></div>
  </div>
  <div class="review-strip">
    <span class="slider-arrow prev"><svg width="10" height="10" viewBox="0 0 10 10"><path d="M7 1 3 5l4 4" fill="none" stroke="#12305a" stroke-width="2"/></svg></span>
    <article class="review-card">
      <div class="review-head"><span class="avatar">J</span><b>John Doe</b></div>
      <p>Always on time and thorough. The office has never looked better, and booking is simple. Friendly team, fair pricing and no fuss at all.</p>
      <div class="review-foot"><i></i><span class="stars">★★★★★</span></div>
    </article>
    <article class="review-card">
      <div class="review-head"><span class="avatar">J</span><b>John Doe</b></div>
      <p>Reliable cleaners who do the job right every single visit. Our rental was spotless for inspection and the team was easy to deal with.</p>
      <div class="review-foot"><i></i><span class="stars">★★★★★</span></div>
    </article>
    <article class="review-card">
      <div class="review-head"><span class="avatar">J</span><b>John Doe</b></div>
      <p>We have used them for years at our clinic. Consistent, careful and honest work, and they always reply quickly when we need extra help.</p>
      <div class="review-foot"><i></i><span class="stars">★★★★★</span></div>
    </article>
    <span class="slider-arrow next"><svg width="10" height="10" viewBox="0 0 10 10"><path d="M3 1l4 4-4 4" fill="none" stroke="#12305a" stroke-width="2"/></svg></span>
  </div>
</section>

<section class="about">
  <div class="about-photo" role="img" aria-label="Two uniformed cleaners with equipment beside the company vans"></div>
  <div class="about-copy">
    <h2>Call the cleaners you can count on.</h2>
    <p>When you need help cleaning, the last thing you want is more stress. Too often, that's exactly what happens —</p>
    <p>Cleaners don't show up, jobs get rushed or half-done. And you're left wondering why you didn't just do it yourself.</p>
    <p>You shouldn't have to second guess whether the job will be done right. You should be able to book it, forget it, and trust it's sorted — properly.</p>
    <p>Trusted by locals for 30+ years to deliver reliable, long-term cleaning — the kind you never have to second-guess.</p>
    <a class="btn-navy" href="#">Learn More ›</a>
  </div>
</section>

<section class="stats">
  <div class="stat">
    <span class="stat-icon"><svg width="32" height="32" viewBox="0 0 32 32"><circle cx="12" cy="11" r="5" fill="#12305a"/><path d="M3 27c0-6 4-9 9-9s9 3 9 9z" fill="#12305a"/><circle cx="23" cy="12" r="4" fill="#12305a"/><path d="M22 18c4 0 7 3 7 8h-6" fill="#12305a"/></svg></span>
    <div><strong>92+</strong><span>Recurring Clients</span></div>
  </div>
  <div class="stat">
    <span class="stat-icon"><svg width="32" height="32" viewBox="0 0 32 32"><rect x="5" y="7" width="22" height="20" rx="2" fill="none" stroke="#b08d43" stroke-width="2.5"/><path d="M5 13h22M11 4v6M21 4v6" stroke="#b08d43" stroke-width="2.5"/></svg></span>
    <div><strong>4,150+</strong><span>Visits Per Year</span></div>
  </div>
  <div class="stat">
    <span class="stat-icon"><svg width="32" height="32" viewBox="0 0 32 32"><path d="M4 16 16 5l12 11v11H4z" fill="none" stroke="#12305a" stroke-width="2.5"/><path d="M11 20l4 4 7-8" fill="none" stroke="#12305a" stroke-width="2.5"/></svg></span>
    <div><strong>265+</strong><span>Pre-Sale / Exit Cleans</span></div>
  </div>
</section>

<section class="services">
  <h2 class="section-title">Our Services</h2>
  <div class="service-grid">
    <a class="service-card featured" href="#" role="img" aria-label="Cleaners in an office shaking hands with a client"><span class="service-label">Commercial Cleaning</span></a>
    <a class="service-card" href="#" role="img" aria-label="Cleaners working in a modern home interior"><span class="service-label">Residential Cleaning</span></a>
    <a class="service-card" href="#" role="img" aria-label="Cleaner washing a large window"><span class="service-label">Window Cleaning</span></a>
    <a class="service-card" href="#" role="img" aria-label="Cleaner steam cleaning a sofa"><span class="service-label">Steam Cleaning</span></a>
  </div>
</section>

<section class="values">
  <h2 class="section-title">Our Core Values</h2>
  <div class="value-row">
    <div class="value-card">
      <svg width="36" height="36" viewBox="0 0 36 36"><path d="M4 18 18 6l14 12v13H4z" fill="#12305a"/><rect x="15" y="22" width="6" height="9" fill="#fff"/></svg>
      <h3>Be Real</h3><p>Open, honest communication</p>
    </div>
    <div class="value-card featured">
      <svg width="36" height="36" viewBox="0 0 36 36"><path d="M8 3h14l7 7v23H8z" fill="#12305a"/><path d="M13 16h11M13 21h11M13 26h7" stroke="#fff" stroke-width="2"/></svg>
      <h3>Do It Right</h3><p>Attention to detail, every time</p>
    </div>
    <div class="value-card">
      <svg width="36" height="36" viewBox="0 0 36 36"><circle cx="13" cy="11" r="5" fill="#12305a"/><circle cx="25" cy="11" r="5" fill="#12305a"/><path d="M4 30c0-7 4-11 9-11s9 4 9 11zM16 30c0-7 4-11 9-11s9 4 9 11z" fill="#12305a"/></svg>
      <h3>Have Fun</h3><p>Friendly teams that care</p>
    </div>
    <div class="value-card">
      <svg width="36" height="36" viewBox="0 0 36 36"><circle cx="18" cy="18" r="14" fill="none" stroke="#12305a" stroke-width="3"/><path d="M11 18l5 5 9-10" fill="none" stroke="#12305a" stroke-width="3"/></svg>
      <h3>Make It Easy</h3><p>Simple booking and clear pricing</p>
    </div>
  </div>
</section>

<footer class="site-footer">
  <div class="contact-row">
    <div class="contact-item">
      <span class="contact-icon"><svg width="20" height="20" viewBox="0 0 20 20"><path d="M10 1a6 6 0 0 0-6 6c0 5 6 12 6 12s6-7 6-12a6 6 0 0 0-6-6z" fill="#0a1a33"/><circle cx="10" cy="7" r="2.2" fill="#fff"/></svg></span>
      <div><b>Address</b><span>18 Harbour Lane<br>Sale Victoria 3850</span></div>
    </div>
    <div class="contact-item">
      <span class="contact-icon"><svg width="20" height="20" viewBox="0 0 20 20"><rect x="2" y="4" width="16" height="12" rx="1.5" fill="#0a1a33"/><path d="M2.5 5l7.5 6 7.5-6" fill="none" stroke="#fff" stroke-width="1.5"/></svg></span>
      <div><b>Email</b><span>info@thornburycleaning-example.com.au</span></div>
    </div>
    <div class="contact-item">
      <span class="contact-icon"><svg width="20" height="20" viewBox="0 0 20 20"><path d="M5 2l3 4-2 2c1 2 3 4 5 5l2-2 4 3-2 4C8 17 3 12 2 5z" fill="#0a1a33"/></svg></span>
      <div><b>Phone</b><span>0400 000 123</span></div>
    </div>
  </div>
  <div class="footer-base">
    <a class="brand" href="#"><span class="brand-name">THORNBURY CLEANING</span><span class="brand-sub">SALE · VIC</span></a>
    <small>© Copyrights 2025 | All Rights Reserved</small>
  </div>
</footer>

</body>
</html>
```